Manufacturing and engineering company needs corporate stationary

Looking for professional stationary to use internally as well as for giveaways for customers. Looking for digital and printed options.

The logo file attached has the overall colour scheme and the logo needs to be used in the stationary. The circle portion of the logo can be used independently. We are open to variations on the colours and style of logo but it should remain very similar to the attached.

Requirements
Must have
• The logo or at the very least the circle portion of the logo
Nice to have
• Would like a powerpoint template, word document template for proposals, printed brochure template
Should not have
• Business cards are not the focus, while you can suggest ideas this is not the focus

```html
<!DOCTYPE html>
<html lang="en">
<head>
<meta charset="utf-8">
<title>Norvale Stationery</title>
<link href="https://fonts.googleapis.com/css2?family=Open+Sans:wght@400;600;700&display=swap" rel="stylesheet">
<style>
  :root {
    --bg: #e6e6e6;
    --paper: #f7f7f7;
    --gold: #b19c68;
    --gold-soft: #c9b78c;
    --grey: #8a8a8a;
    --ink: #6e6e6e;
    --white: #ffffff;
  }
  * { margin: 0; padding: 0; box-sizing: border-box; }
  html, body { width: 1200px; height: 795px; overflow: hidden; }
  body { background: var(--bg); font-family: "Open Sans", Arial, sans-serif; color: var(--ink); position: relative; }

  .sheet { position: absolute; background: var(--paper); }
  .brand { position: absolute; display: flex; align-items: center; }
  .brand-dot { border-radius: 50%; background: var(--grey); flex: none; }
  .brand-name { font-weight: 700; color: var(--ink); line-height: 1; }

  .footer-rule { position: absolute; left: 0; right: 0; bottom: 0; height: 3px; background: var(--grey); }
  .footer-tab {
    position: absolute; right: 0; bottom: 0; background: var(--gold); color: var(--white);
    clip-path: polygon(8% 0, 100% 0, 100% 100%, 0 100%);
    display: flex; align-items: center; justify-content: center; letter-spacing: 1.2px;
  }

  .contact { position: absolute; font-size: 4.6px; line-height: 6.6px; color: var(--ink); }
  .contact-line { display: flex; align-items: center; gap: 2px; }
  .contact-icon { width: 4px; height: 4px; fill: var(--gold); }

  /* Letterhead */
  .letterhead { left: 292px; top: 99px; width: 293px; height: 415px; }
  .letterhead .brand { left: 20px; top: 24px; gap: 4px; }
  .letterhead .brand-dot { width: 26px; height: 26px; }
  .letterhead .brand-name { font-size: 13px; }
  .letterhead .contact { left: 20px; top: 368px; }
  .letterhead .footer-tab { width: 90px; height: 11px; font-size: 4.5px; }

  /* Folder */
  .folder { left: 635px; top: 80px; width: 347px; height: 437px; background: var(--gold); }
  .folder-spine { position: absolute; left: 6px; top: 0; bottom: 0; width: 8px; border-left: 1px solid rgba(255,255,255,.25); border-right: 1px solid rgba(255,255,255,.25); }
  .folder .brand { left: 60px; top: 192px; gap: 6px; }
  .folder .brand-dot { width: 70px; height: 70px; background: var(--white); }
  .folder .brand-name { font-size: 27px; color: var(--white); }

  /* Business cards */
  .card { left: 186px; width: 133px; height: 75px; }
  .card-front { top: 550px; }
  .card-front .brand { left: 15px; top: 29px; gap: 2px; }
  .card-front .brand-dot { width: 14px; height: 14px; }
  .card-front .brand-name { font-size: 7.5px; }
  .card-divider { position: absolute; left: 69px; top: 13px; width: 1px; height: 44px; background: #cfcfcf; }
  .card-person { position: absolute; left: 74px; top: 16px; font-size: 4.6px; line-height: 5.5px; }
  .card-person .name { color: var(--gold); font-weight: 700; font-size: 5px; }
  .card-person .contact { position: static; margin-top: 3px; font-size: 3.8px; line-height: 5px; }
  .card-front .footer-tab { width: 63px; height: 7px; font-size: 3.6px; }
  .card-back { top: 647px; background: var(--gold); }
  .card-back .brand { left: 0; right: 0; top: 17px; justify-content: center; gap: 3px; }
  .card-back .brand-dot { width: 30px; height: 30px; background: var(--white); }
  .card-back .brand-name { font-size: 9px; color: var(--white); }
  .card-back .card-web { position: absolute; left: 0; right: 0; bottom: 5px; text-align: center; font-size: 3.8px; letter-spacing: 1.5px; color: var(--white); }

  /* Envelopes */
  .envelope { top: 562px; width: 328px; height: 156px; }
  .envelope-front { left: 354px; }
  .envelope-front .brand { left: 13px; top: 12px; gap: 3px; }
  .envelope-front .brand-dot { width: 28px; height: 28px; }
  .envelope-front .brand-name { font-size: 12px; }
  .envelope-front .contact { left: 13px; top: 128px; font-size: 4.8px; }
  .envelope-front .footer-tab { width: 100px; height: 12px; font-size: 5px; }
  .envelope-back { left: 714px; }
  .envelope-flap { position: absolute; left: 0; top: 0; width: 328px; height: 56px; }
  .envelope-back .brand { left: 0; right: 0; top: 12px; justify-content: center; gap: 3px; }
  .envelope-back .brand-dot { width: 32px; height: 32px; background: var(--white); }
  .envelope-back .brand-name { font-size: 10px; color: var(--white); }
</style>
</head>
<body>

  <!-- Letterhead -->
  <section class="sheet letterhead">
    <div class="brand"><span class="brand-dot"></span><span class="brand-name">Norvale</span></div>
    <div class="contact">
      <div>1420 Cedar Row</div>
      <div>Lakeport, Oregon 97400</div>
      <div class="contact-line"><svg class="contact-icon" viewBox="0 0 10 10"><path d="M2 1h2l1 2.5-1.3 1A6 6 0 0 0 6 7.3l1-1.3L9.5 7v2C5 9.5.5 5 1 1z"/></svg>555 210 4817</div>
      <div class="contact-line"><svg class="contact-icon" viewBox="0 0 10 10"><rect x="1" y="4" width="8" height="5"/><rect x="3" y="1" width="4" height="3"/></svg>555 742 0318</div>
      <div class="contact-line"><svg class="contact-icon" viewBox="0 0 10 10"><rect x="1" y="2" width="8" height="6"/></svg>mail@norvale.example</div>
    </div>
    <div class="footer-rule"></div>
    <div class="footer-tab">www.norvale.example</div>
  </section>

  <!-- Presentation folder -->
  <section class="sheet folder" role="img" aria-label="Folder cover in gold with a scattered leaf pattern and the Norvale name">
    <div class="folder-spine"></div>
    <div class="brand"><span class="brand-dot"></span><span class="brand-name">Norvale</span></div>
  </section>

  <!-- Business card, front -->
  <section class="sheet card card-front">
    <div class="brand"><span class="brand-dot"></span><span class="brand-name">Norvale</span></div>
    <div class="card-divider"></div>
    <div class="card-person">
      <div class="name">Alan Reed</div>
      <div>CEO/Founder</div>
      <div class="contact">
        <div>1420 Cedar Row</div>
        <div>Lakeport, Oregon 97400</div>
        <div class="contact-line"><svg class="contact-icon" viewBox="0 0 10 10"><path d="M2 1h2l1 2.5-1.3 1A6 6 0 0 0 6 7.3l1-1.3L9.5 7v2C5 9.5.5 5 1 1z"/></svg>555 210 4817</div>
        <div class="contact-line"><svg class="contact-icon" viewBox="0 0 10 10"><rect x="1" y="4" width="8" height="5"/><rect x="3" y="1" width="4" height="3"/></svg>555 742 0318</div>
        <div class="contact-line"><svg class="contact-icon" viewBox="0 0 10 10"><rect x="1" y="2" width="8" height="6"/></svg>mail@norvale.example</div>
      </div>
    </div>
    <div class="footer-rule"></div>
    <div class="footer-tab">www.norvale.example</div>
  </section>

  <!-- Business card, back -->
  <section class="sheet card card-back">
    <div class="brand"><span class="brand-dot"></span><span class="brand-name">Norvale</span></div>
    <div class="card-web">www.norvale.example</div>
  </section>

  <!-- Envelope, front -->
  <section class="sheet envelope envelope-front">
    <div class="brand"><span class="brand-dot"></span><span class="brand-name">Norvale</span></div>
    <div class="contact">
      <div>1420 Cedar Row</div>
      <div>Lakeport, Oregon 97400</div>
    </div>
    <div class="footer-rule"></div>
    <div class="footer-tab">www.norvale.example</div>
  </section>

  <!-- Envelope, back -->
  <section class="sheet envelope envelope-back">
    <svg class="envelope-flap" viewBox="0 0 328 56" aria-hidden="true">
      <polygon points="0,0 328,0 322,56 6,56" fill="#b19c68"/>
    </svg>
    <div class="brand"><span class="brand-dot"></span><span class="brand-name">Norvale</span></div>
  </section>

</body>
</html>
```